VelloCap Nutrition Require Label Design Assistance

We are VelloCap!

We are a new mushroom focused nutrition supplement company looking for some design assistance. We are looking to provide some of the highest quality mushroom supplements available on the market today, using 100% fruiting bodies where many other companies opt for cheaper alternatives. We strongly believe in the power of mushroom nutrition and wish to focus on the high-end supplement market.

We are starting with three initial ranges; Lions Mane, Turkey Tail and Reishi - and wish to have powerful yet elegant designs for each. We wish to be visually appealing whilst maintaining the high-end feel. Imagery of the mushrooms on the label would be good if it maintains high-end appeal. Our bottles will be dark green and lids will be white if this helps with visualization. We have a logo and preferred font for the name which can be used if possible. The image in the logo may need resizing to fit with the supplement market (smaller logo/larger font). If you provide a superior logo to that which we currently have, we would consider using it.

The three range designs should be the same, but with the mushroom name and any imagery changed to reflect the different ranges. I am happy to supply images where required.

Label dimensions = 55mm x 150mm

Target Market(s)

Premium High End Health Supplements

Industry/Entity Type

Supplement

Font styles to use
Serif
Sans Serif

Colors

Designer to choose colors to be used in the design.

Requirements
Must have
• Must have the text "100% Fruiting Bodies"
• Must have Organic + Vegan notification.
• Must have an ingredients section, and there will need to be some space for small-print (which will be decided on shortly).
Nice to have
• See label specifications in message thread.

```html
<!DOCTYPE html>
<html lang="en">
<head>
<meta charset="utf-8">
<title>VelloCap Turkey Tail Label – Colour Options</title>
<link rel="stylesheet" href="https://fonts.googleapis.com/css2?family=Cinzel:wght@700;900&family=Lato:wght@400;700&display=swap">
<style>
  :root {
    --canvas: #000000;
    --paper: #ffffff;
    --brown: #7a4f2c;
    --brown-dark: #5a3414;
    --brown-light: #8e5f31;
    --brown-box: #d2b190;
    --green: #1d6d3a;
    --green-dark: #14552b;
    --green-light: #45b862;
    --green-box: #b6dfbb;
  }
  * { margin: 0; padding: 0; box-sizing: border-box; }
  html, body { width: 1200px; height: 1200px; overflow: hidden; background: var(--canvas); }
  body { position: relative; font-family: "Lato", sans-serif; }

  .label {
    position: absolute; left: 107px; width: 1009px; height: 371px;
    background: var(--paper); overflow: hidden;
  }
  .label--brown { top: 157px; --ink: var(--brown); --ink-dark: var(--brown-dark); --ink-light: var(--brown-light); --box: var(--brown-box); }
  .label--green { top: 673px; --ink: var(--green); --ink-dark: var(--green-dark); --ink-light: var(--green-light); --box: var(--green-box); }

  .label__art { position: absolute; inset: 0; }
  .abs { position: absolute; }

  .brand {
    position: absolute; display: flex; flex-direction: column; align-items: center;
    font-family: "Cinzel", serif; font-weight: 700; color: var(--ink); letter-spacing: 0.5px;
  }
  .brand__dot { width: 26px; height: 26px; border-radius: 50%; background: var(--ink); margin-bottom: 6px; }
  .brand--side { left: 115px; top: 42px; width: 100px; font-size: 14px; }
  .brand--front { left: 444px; top: 24px; width: 120px; font-size: 16px; }
  .brand--front .brand__dot { width: 30px; height: 30px; margin-bottom: 10px; }

  .about {
    left: 29px; top: 99px; width: 271px; height: 109px;
    border: 1px solid var(--ink); padding: 5px 8px;
    font-size: 11px; line-height: 14.2px; color: var(--ink); text-align: justify;
  }
  .batch-note { left: 29px; top: 213px; font-size: 9.3px; color: var(--ink); }
  .address { left: 29px; top: 233px; font-size: 11px; line-height: 14.4px; color: var(--ink); }
  .batch-labels { left: 29px; top: 287px; font-size: 11px; line-height: 14.8px; color: var(--ink); }
  .batch-box { left: 124px; top: 288px; width: 131px; height: 45px; background: var(--box); }

  .title {
    left: 300px; top: 98px; width: 408px; text-align: center;
    font-family: "Cinzel", serif; font-weight: 900; font-size: 38px; line-height: 40px; letter-spacing: -0.5px;
    background: linear-gradient(180deg, var(--ink-dark), var(--ink-light) 55%, var(--ink-dark));
    -webkit-background-clip: text; background-clip: text; color: transparent;
  }
  .subtitle { left: 300px; top: 135px; width: 408px; text-align: center; font-size: 10px; letter-spacing: 0.3px; color: var(--ink); }
  .fruiting { left: 398px; top: 350px; width: 200px; text-align: center; font-size: 14px; line-height: 17px; color: var(--paper); }

  .capsules {
    left: 586px; top: 296px; height: 14px; width: 48px;
    border: 1px solid var(--ink); border-radius: 8px; background: var(--paper);
    font-size: 6px; line-height: 12px; padding-left: 4px; color: var(--ink); letter-spacing: 0.2px;
  }
  .capsules__count {
    position: absolute; right: -11px; top: -3px; width: 19px; height: 19px; border-radius: 50%;
    border: 1px solid var(--ink); background: var(--paper);
    font-size: 10px; font-weight: 700; line-height: 17px; text-align: center;
  }

  .photo {
    left: 340px; top: 200px; width: 168px; height: 121px; border-radius: 50%;
    background: radial-gradient(ellipse at 55% 50%, #8a6440, #5b3b22 60%, rgba(110,80,55,0.5) 85%, transparent 100%);
  }

  .facts { left: 709px; top: 0; width: 271px; color: var(--paper); }
  .facts__heading { position: absolute; left: 0; top: 42px; width: 275px; text-align: center; font-family: "Cinzel", serif; font-weight: 700; font-size: 17px; letter-spacing: 0.5px; }
  .facts__direction { position: absolute; left: 0; top: 75px; font-size: 11px; white-space: nowrap; }
  .ingredients { position: absolute; left: 0; top: 95px; width: 271px; border: 1px solid var(--paper); border-collapse: collapse; font-size: 11px; }
  .ingredients td { border-bottom: 1px solid var(--paper); padding: 0 5px; height: 18.6px; }
  .ingredients .ingredients__head td { font-weight: 700; height: 21px; }
  .warnings { position: absolute; left: 0; top: 201px; width: 271px; height: 55px; border: 1px solid var(--paper); padding: 4px 5px; font-size: 11px; line-height: 14.2px; }
  .storage { position: absolute; left: 0; top: 258px; font-size: 9.3px; font-weight: 700; white-space: nowrap; }
  .badge { position: absolute; top: 289px; width: 38px; height: 38px; border-radius: 50%; border: 2px solid var(--paper); }
  .badge--vegan { left: 0; }
  .badge--organic { left: 50px; }
  .badge--recycle { left: 108px; width: 30px; height: 30px; top: 293px; background: var(--paper); }
  .code-space { position: absolute; left: 154px; top: 283px; width: 116px; height: 51px; background: var(--paper); }
</style>
</head>
<body>

<section class="label label--brown">
  <svg class="label__art" width="1009" height="371" viewBox="0 0 1009 371" aria-hidden="true">
    <path d="M684,0 C650,170 560,300 334,371 L1009,371 L1009,0 Z" fill="#7a4f2c"/>
    <path d="M713,0 C695,140 620,230 480,320" fill="none" stroke="#ffffff" stroke-width="6"/>
    <path d="M365,371 C390,360 415,345 440,330" fill="none" stroke="#ffffff" stroke-width="5"/>
    <ellipse cx="424" cy="260" rx="101" ry="80" fill="#7a4f2c"/>
    <ellipse cx="424" cy="260" rx="92" ry="71" fill="#ffffff"/>
  </svg>
  <div class="abs photo" role="img" aria-label="Photograph of layered turkey tail mushroom caps"></div>

  <div class="brand brand--side"><span class="brand__dot"></span>VelloCap</div>
  <p class="abs about">Lorem ipsum dolor sit amet, consectetur adipiscing elit, sed do eiusmod tempor incididunt ut labore et dolore magna aliqua. Ut enim ad minim veniam, quis nostrud exercitation ullamco laboris nisi ut aliquip ex ea commodo consequat. Duis aute irure dolor in reprehenderit in voluptate velit esse cillum dolore eu fugiat nulla pariatur.</p>
  <p class="abs batch-note">Batch number and best before: See base</p>
  <p class="abs address">Address line,<br>Country, 1234, VIC<br>www.companyname.com</p>
  <p class="abs batch-labels">Batch Number<br>Best Before</p>
  <div class="abs batch-box"></div>

  <div class="brand brand--front"><span class="brand__dot"></span>VelloCap</div>
  <h1 class="abs title">TURKEY TAIL</h1>
  <p class="abs subtitle">FOOD SUPPLEMENT</p>
  <div class="abs capsules">CAPSULES<span class="capsules__count">60</span></div>
  <p class="abs fruiting">100% Fruiting Bodies</p>

  <div class="abs facts">
    <h2 class="facts__heading">SUPPLEMENT FACTS</h2>
    <p class="facts__direction">DIRECTION: Serving Size 2 Capsules</p>
    <table class="ingredients">
      <tr class="ingredients__head"><td>INGREDIENTS:</td></tr>
      <tr><td>Turkey Tail Organic Fruiting Bodies</td></tr>
      <tr><td>Organic Enoki Extract</td></tr>
      <tr><td>Curcumin Extract</td></tr>
      <tr><td>Black Pepper</td></tr>
    </table>
    <p class="warnings">WARNINGS: Do not exceed stated recommended dose.A food supplement should not be used as a substitute for a varied diet.</p>
    <p class="storage">*Store in a cool place, out of reach and sight of children.</p>
    <span class="badge badge--vegan"></span>
    <span class="badge badge--organic"></span>
    <span class="badge badge--recycle"></span>
    <div class="code-space"></div>
  </div>
</section>

<section class="label label--green">
  <svg class="label__art" width="1009" height="371" viewBox="0 0 1009 371" aria-hidden="true">
    <defs>
      <linearGradient id="greenPanel" x1="0" y1="0" x2="1" y2="1">
        <stop offset="0" stop-color="#14552b"/>
        <stop offset="0.45" stop-color="#45b862"/>
        <stop offset="1" stop-color="#1d6d3a"/>
      </linearGradient>
      <linearGradient id="greenRing" x1="0" y1="0" x2="1" y2="1">
        <stop offset="0" stop-color="#14552b"/>
        <stop offset="0.5" stop-color="#45b862"/>
        <stop offset="1" stop-color="#14552b"/>
      </linearGradient>
    </defs>
    <path d="M684,0 C650,170 560,300 334,371 L1009,371 L1009,0 Z" fill="url(#greenPanel)"/>
    <path d="M713,0 C695,140 620,230 480,320" fill="none" stroke="#ffffff" stroke-width="6"/>
    <path d="M365,371 C390,360 415,345 440,330" fill="none" stroke="#ffffff" stroke-width="5"/>
    <ellipse cx="424" cy="260" rx="101" ry="80" fill="url(#greenRing)"/>
    <ellipse cx="424" cy="260" rx="92" ry="71" fill="#ffffff"/>
  </svg>
  <div class="abs photo" role="img" aria-label="Photograph of layered turkey tail mushroom caps"></div>

  <div class="brand brand--side"><span class="brand__dot"></span>VelloCap</div>
  <p class="abs about">Lorem ipsum dolor sit amet, consectetur adipiscing elit, sed do eiusmod tempor incididunt ut labore et dolore magna aliqua. Ut enim ad minim veniam, quis nostrud exercitation ullamco laboris nisi ut aliquip ex ea commodo consequat. Duis aute irure dolor in reprehenderit in voluptate velit esse cillum dolore eu fugiat nulla pariatur.</p>
  <p class="abs batch-note">Batch number and best before: See base</p>
  <p class="abs address">Address line,<br>Country, 1234, VIC<br>www.companyname.com</p>
  <p class="abs batch-labels">Batch Number<br>Best Before</p>
  <div class="abs batch-box"></div>

  <div class="brand brand--front"><span class="brand__dot"></span>VelloCap</div>
  <h1 class="abs title">TURKEY TAIL</h1>
  <p class="abs subtitle">FOOD SUPPLEMENT</p>
  <div class="abs capsules">CAPSULES<span class="capsules__count">60</span></div>
  <p class="abs fruiting">100% Fruiting Bodies</p>

  <div class="abs facts">
    <h2 class="facts__heading">SUPPLEMENT FACTS</h2>
    <p class="facts__direction">DIRECTION: Serving Size 2 Capsules</p>
    <table class="ingredients">
      <tr class="ingredients__head"><td>INGREDIENTS:</td></tr>
      <tr><td>Turkey Tail Organic Fruiting Bodies</td></tr>
      <tr><td>Organic Enoki Extract</td></tr>
      <tr><td>Curcumin Extract</td></tr>
      <tr><td>Black Pepper</td></tr>
    </table>
    <p class="warnings">WARNINGS: Do not exceed stated recommended dose.A food supplement should not be used as a substitute for a varied diet.</p>
    <p class="storage">*Store in a cool place, out of reach and sight of children.</p>
    <span class="badge badge--vegan"></span>
    <span class="badge badge--organic"></span>
    <span class="badge badge--recycle"></span>
    <div class="code-space"></div>
  </div>
</section>

</body>
</html>
```